Carivo Disposal Franchise LLC Informational Catalogue/Flipbook

We are seeking a professional, yet inviting informational catalogue/flipbook on owning a medical waste franchise with Carivo Disposal Franchise LLC. Our vision is to print this catalogue in color, landscape orientation, spiral-bound, and about 6in x 9in in size.
For branding continuity, please refer to our website: www.carivo-example.com.
Attached please find the text copy, organized by page, as well as a .zip folder containing photos that can be used throughout the catalogue. Not all of the photos have to be used, so chose at your own discretion.

```html
<!DOCTYPE html>
<html lang="en">
<head>
<meta charset="utf-8">
<title>Carivo Disposal Franchise – Catalogue Spreads</title>
<link href="https://fonts.googleapis.com/css2?family=Fira+Sans+Condensed:wght@400;500&family=Fira+Sans:wght@700&display=swap" rel="stylesheet">
<style>
  :root{
    --sheet:#bdbdbd;
    --ink:#111111;
    --red-light:#e87174;
    --red-deep:#d9262b;
    --red-title:#d7252a;
    --white:#ffffff;
    --tick:#3aa53a;
    --body-dark:#1a1a1a;
    --brick:#93625a;
    --brick-soft:#a47a6e;
    --hall-light:#e3f2f0;
    --hall-mid:#a9d3ce;
  }
  *{margin:0;padding:0;box-sizing:border-box}
  html,body{width:1200px;height:848px;overflow:hidden;background:var(--sheet)}
  body{position:relative;font-family:"Fira Sans Condensed",sans-serif}
  .page-label{position:absolute;width:200px;text-align:center;font-family:"Fira Sans",sans-serif;font-weight:700;font-size:19px;color:var(--ink);letter-spacing:.3px}
  .spread{position:absolute;left:152px;width:896px;height:298px;display:flex;box-shadow:4px 5px 6px rgba(0,0,0,.35)}
  .page{position:relative;width:448px;height:298px;overflow:hidden}
  .page--red{background:linear-gradient(90deg,var(--red-light),var(--red-deep))}
  .photo-hospital{position:absolute;inset:0;background:linear-gradient(135deg,var(--brick-soft),var(--brick))}
  .photo-hallway{position:absolute;inset:0;background:radial-gradient(ellipse at 60% 40%,var(--hall-light) 0%,var(--hall-mid) 100%)}
  .heading{position:absolute;left:30px;top:50px;font-size:15px;font-weight:500;color:var(--red-title);white-space:nowrap}
  .service-list{position:absolute;top:76px;list-style:none;color:var(--white);font-size:7.3px;font-weight:400}
  .service-list li{height:20.4px;line-height:9px;position:relative;padding-left:7px;white-space:nowrap}
  .service-list li::before,.industry-list li::before{content:"";position:absolute;left:0;top:3.5px;width:2px;height:2px;border-radius:50%;background:currentColor}
  .service-list--one{left:31px}
  .service-list--two{left:176px}
  .industry-heading{left:55px;top:51px}
  .industry-panel{position:absolute;left:51px;top:69px;width:344px;height:168px;background:rgba(255,255,255,.6)}
  .industry-list{position:absolute;top:4px;list-style:none;color:var(--body-dark);font-size:7.2px;font-weight:400}
  .industry-list li{height:12.45px;line-height:9px;position:relative;padding-left:7px;white-space:nowrap}
  .industry-list li.more{padding-left:0;margin-left:-8px}
  .industry-list li.more::before{display:none}
  .industry-list--a{left:6px}
  .industry-list--b{left:140px}
  .industry-list--c{left:273px}
  .benefit-list{position:absolute;left:30px;top:73px;list-style:none;color:var(--white);font-size:8.8px;font-weight:400}
  .benefit-list li{height:22.5px;display:flex;align-items:center;gap:7px;white-space:nowrap}
  .check{width:11px;height:11px;flex:none}
</style>
</head>
<body>
  <div class="page-label" style="left:273px;top:40px">PAGE 2</div>
  <div class="page-label" style="left:727px;top:40px">PAGE 3</div>
  <div class="page-label" style="left:273px;top:434px">PAGE 4</div>
  <div class="page-label" style="left:727px;top:434px">PAGE 5</div>

  <section class="spread" style="top:75px">
    <div class="page">
      <div class="photo-hospital" role="img" aria-label="Photo of a hospital entrance sign on a brick wall in front of the hospital building"></div>
    </div>
    <div class="page page--red">
      <h2 class="heading">Our Services</h2>
      <ul class="service-list service-list--one">
        <li>Medical Waste Management &amp; Disposal</li>
        <li>Pharmaceutical Waste Disposal</li>
        <li>Chemotherapy Waste Disposal</li>
        <li>Pathological Waste Disposal</li>
        <li>Universal Waste Disposal</li>
        <li>Hazardous Waste Disposal</li>
      </ul>
      <ul class="service-list service-list--two">
        <li>Mailback Programs</li>
        <li>PPE Supplies</li>
        <li>Sharps Containers</li>
        <li>OSHA Safety &amp; Compliance Training</li>
        <li>Document Shredding &amp; Media Destruction</li>
      </ul>
    </div>
  </section>

  <section class="spread" style="top:473px">
    <div class="page">
      <div class="photo-hallway" role="img" aria-label="Blurred photo of a bright teal hospital corridor"></div>
      <h2 class="heading industry-heading">Industries We Serve</h2>
      <div class="industry-panel">
        <ul class="industry-list industry-list--a">
          <li>Animal orphanages</li><li>Allergists</li><li>Assisted living homes</li><li>Blood banks</li><li>Casinos</li><li>Colleges &amp; Universities</li><li>Clinics</li><li>Dentists</li><li>Diagnostic centers</li><li>Dialysis centers</li><li>Doctors</li><li>Endo centers</li><li>Funeral homes</li>
        </ul>
        <ul class="industry-list industry-list--b">
          <li>Government agencies</li><li>Health centers &amp; departments</li><li>Hematologists / Oncologists</li><li>Hospitals</li><li>Hospital satellite facilities</li><li>Imaging centers</li><li>Laboratories</li><li>Nursing homes</li><li>OB/GYN's</li><li>Oral surgeons</li><li>Outpatient surgery centers</li><li>Pediatricians</li><li>Pharmaceutical manufacturers</li>
        </ul>
        <ul class="industry-list industry-list--c">
          <li>Physicians</li><li>Prisons</li><li>Radiology facilities</li><li>Schools</li><li>Tattoo parlors</li><li>Testing centers</li><li>Urologists</li><li>Veterinarians</li><li class="more">and More!</li>
        </ul>
      </div>
    </div>
    <div class="page page--red">
      <h2 class="heading">Why Franchise With Carivo?</h2>
      <ul class="benefit-list">
        <li><svg class="check" viewBox="0 0 11 11"><rect width="11" height="11" fill="var(--white)"/><path d="M2 5.8 4.4 8.4 9.5 1.8" fill="none" stroke="var(--tick)" stroke-width="1.8"/></svg>Low Up-Front Investment</li>
        <li><svg class="check" viewBox="0 0 11 11"><rect width="11" height="11" fill="var(--white)"/><path d="M2 5.8 4.4 8.4 9.5 1.8" fill="none" stroke="var(--tick)" stroke-width="1.8"/></svg>Low Competition</li>
        <li><svg class="check" viewBox="0 0 11 11"><rect width="11" height="11" fill="var(--white)"/><path d="M2 5.8 4.4 8.4 9.5 1.8" fill="none" stroke="var(--tick)" stroke-width="1.8"/></svg>Recession Resistant</li>
        <li><svg class="check" viewBox="0 0 11 11"><rect width="11" height="11" fill="var(--white)"/><path d="M2 5.8 4.4 8.4 9.5 1.8" fill="none" stroke="var(--tick)" stroke-width="1.8"/></svg>Diversified Service Offerings</li>
        <li><svg class="check" viewBox="0 0 11 11"><rect width="11" height="11" fill="var(--white)"/><path d="M2 5.8 4.4 8.4 9.5 1.8" fill="none" stroke="var(--tick)" stroke-width="1.8"/></svg>Technology Driven</li>
        <li><svg class="check" viewBox="0 0 11 11"><rect width="11" height="11" fill="var(--white)"/><path d="M2 5.8 4.4 8.4 9.5 1.8" fill="none" stroke="var(--tick)" stroke-width="1.8"/></svg>A Client Focused Brand</li>
      </ul>
    </div>
  </section>
</body>
</html>
```